Need a cover for eBook:
Title is: 41 Blunders That Sink Your Indie-Released Volume.
Remarks about the title: I know that is difficult to design a cover with a number. You can add the word TOP (in caps or not) before 41 blunders. It is not mandatory to insert the word TOP. It is up to you if you think you can create a better cover.
Subtitle is: A Newcomer's Manual for Releasing Solo, Arranging Pictures and Words, Planning Pages, Boosting Sign-ups and Moving More Copies
Author: Dennis R. Walbrey
Publisher: Quillmark Press
The book made the presentation of errors that can occur during the production of an ebook. Title must be big, the title should be readable even when the image is reduced in size. No photo please.
I join my projects as an example. Do what you want but I need impact.

Target Market(s)

Book to sell first at Brimfold Reader Shop. Target is authors, men or women, who want to produce ebooks.

Industry/Entity Type

Publishing Company

Font styles to use
Sans Serif

Colors
3176b5
9bcb3c

Requirements
Must have
• High readability when cover is small.
• Here is the definition of the word KILL
• put an end to or cause the failure or defeat of (something).
• "the committee voted to kill the project"
• synonyms: destroy, put an end to, end, extinguish, dash, quash, ruin, wreck, shatter, smash, crush, scotch, thwart; informalput the kibosh on, stymie, scuttle
• "this would kill all hopes of progress"
• veto, defeat, vote down, rule against, reject, throw out, overrule, overturn, put a stop to, quash, squash
• "an opposition attempt to kill the bill"
Nice to have
• I suggested 2 colors but you can you use another one or two. I want cover that sell. There is so bright ideas here. Come on down!
Should not have
• No picture or photo. If a photo or an object had power to the cover, you can insert one. I don't want a photo-collage.

```html
<!DOCTYPE html>
<html lang="en">
<head>
<meta charset="utf-8">
<title>41 Blunders That Sink Your Indie-Released Volume — Dennis R. Walbrey</title>
<link href="https://fonts.googleapis.com/css2?family=Saira+Condensed:wght@600;700;800&display=swap" rel="stylesheet">
<style>
  :root {
    --cover-blue: #1b6fb0;
    --band-black: #000000;
    --accent-orange: #ff6a13;
    --title-green: #99ff00;
    --text-white: #ffffff;
    --shadow-black: #000000;
    --figure-dark: #0a1620;
  }
  * { margin: 0; padding: 0; box-sizing: border-box; }
  html, body { width: 746px; height: 1200px; overflow: hidden; background: var(--cover-blue); }
  .cover {
    position: relative;
    width: 746px;
    height: 1200px;
    background: var(--cover-blue);
    font-family: "Saira Condensed", "Arial Narrow", sans-serif;
    overflow: hidden;
  }
  .author-band {
    position: absolute;
    left: 0; top: 0;
    width: 746px; height: 90px;
    background: var(--band-black);
    display: flex; align-items: center; justify-content: center;
    font-size: 54px; font-weight: 700; letter-spacing: 0.5px;
    color: var(--text-white);
  }
  .author-band .first-name { color: var(--accent-orange); margin-right: 12px; }
  .hanging-figure {
    position: absolute;
    left: 40px; top: 90px;
    width: 170px; height: 910px;
    background: linear-gradient(180deg, #1a3a55 0%, var(--figure-dark) 20%, var(--figure-dark) 100%);
    border-radius: 40px 40px 20px 20px;
  }
  .title-number {
    position: absolute;
    left: 290px; top: 190px;
    width: 440px;
    text-align: center;
    font-size: 470px; font-weight: 800; line-height: 1;
    color: var(--title-green);
    text-shadow: -6px 6px 0 var(--shadow-black);
    letter-spacing: -4px;
  }
  .title-word {
    position: absolute;
    left: 276px; top: 578px;
    width: 470px;
    text-align: center;
    font-size: 118px; font-weight: 800; line-height: 1;
    color: var(--text-white);
    text-shadow: -4px 4px 0 var(--shadow-black);
  }
  .title-rest {
    position: absolute;
    left: 276px; top: 704px;
    width: 470px;
    text-align: center;
    font-size: 56px; font-weight: 700; line-height: 1.07;
    color: var(--title-green);
    text-shadow: -2px 2px 0 var(--shadow-black);
  }
  .subtitle {
    position: absolute;
    left: 276px; top: 852px;
    width: 470px;
    text-align: center;
    font-size: 25px; font-weight: 600; line-height: 1.2;
    color: var(--text-white);
    padding: 0 14px;
  }
  .publisher {
    position: absolute;
    left: 0; top: 1080px;
    width: 746px;
    text-align: center;
    font-size: 56px; font-weight: 700; line-height: 1;
    color: var(--text-white);
  }
  .publisher .imprint-first { color: var(--accent-orange); }
</style>
</head>
<body>
  <main class="cover">
    <header class="author-band">
      <span class="first-name">Dennis</span><span class="last-name">R. Walbrey</span>
    </header>

    <div class="hanging-figure" role="img" aria-label="Black silhouette of a man hanging from a white rope noose"></div>

    <h1 class="title">
      <span class="title-number">41</span>
      <span class="title-word">BLUNDERS</span>
      <span class="title-rest">THAT SINK YOUR INDIE-<br>RELEASED VOLUME</span>
    </h1>

    <p class="subtitle">A Newcomer's Manual for Releasing Solo, Arranging Pictures and Words, Planning Pages, Boosting Sign-ups and Moving More Copies</p>

    <footer class="publisher">
      <span class="imprint-first">Quillmark</span> Press
    </footer>
  </main>
</body>
</html>
```